Modern and sophisticated web design for architect/designer

Lumo Vant is a Building Design & Drafting studio based in Nedlands Western Australia, providing a high quality and complete client service from concept design through Council planning approvals and building licenses to construction drawings for kitchens and bathrooms, extensions, additions, renovations and new homes.

Lumo Vant is looking for a new qwerty design that *is different from a normal* 2/3 column website. The website design must be very arty, clean and catchy. This design needs to be very different and must not look like a downloadable template.

The design must be able to display a lot of photos for the different projects.

The design must comply with W3C standards (i.e. use of fonts) and must be delivered to us in A PSD layered format.

Here are a couple of example website designs that exemplify what I am after:
1) http://www.prtd.com.au/
2) http://www.martinholsbyarchitect.com/en/
3) http://veromiks.com/

I particularly like numbers 1 and 2. The third, Veromiks, jumps around a little between pages as it is actually several companies. I prefer the page design to remain steady if possible.

I like the very clever nature of number 1 (PRTD). It captures the interest, although slightly gimmicky, however I think it doesn't overpower. Its modern, and visual.

I like the clean elegant design of number 2 (Holsby), it simply delivers everything necessary in a clear intelligent manner, its attractive, menu is clever simple to use and attractive.

I would be very happy to have either of these websites.

here is another one:
4) http://www.tqarchitect.com.au/

Although this is similarly elegant, it appears quite dated. I don't like the thumbnails that you click on in the gallery, its quite clumsy. It looks minimalist, and IS minimalist, doesn't look like there is much option to expand other than changing the pictures.

If you look at my own website:
http://www.lumovant.com.au

I designed and built it myself without any skills or experience. I had to use a generic photo album generator which was worse than useless, the point I am trying to make is I tried to make the menu system a little unusual, I tried to keep the pages neat and tidy, and totally used the "black website" method. However I am more inclined to go with the lighter/white pages of (1) and (2) above because they tend to show photos better.

Dear Designers. 

ArtHive Administration has worked to provide a more comprehensive brief. Please review the amended description. 

Kind Regards, Wesley. 

Target Market(s)

Target market is people who are looking to renovate their home

Industry/Entity Type

Construction

Requirements
Must have
• The brief is to design a visual modern, elegant, sophisticated website for a small scale designer/photographer/architect that looks itself like it is designed. Not off the shelf, simple and dated. Basically the design itself has to exemplify me, it has to say "this guy is a designer, and he is good at it".

```html
<!DOCTYPE html>
<html lang="en">
<head>
<meta charset="utf-8">
<title>Lumo Vant Design</title>
<link href="https://fonts.googleapis.com/css2?family=Open+Sans:wght@400;600;700&display=swap" rel="stylesheet">
<style>
:root{
  --white:#ffffff;
  --bar:#343434;
  --dark:#292929;
  --ink:#555555;
  --ink-soft:#666666;
  --nav-active:#f0f0f0;
  --accent-green:#5cb30e;
  --orange:#fd6450;
  --purple:#9e70d8;
  --lime:#a9ba0c;
  --sky:#0bbce7;
  --tweet:#4a8ec9;
  --social:#4f7fb8;
}
*{margin:0;padding:0;box-sizing:border-box}
html,body{width:1200px;height:1000px;overflow:hidden;background:var(--white)}
body{font-family:"Open Sans",Arial,sans-serif;position:relative}
.canvas{position:relative;width:1200px;height:1000px;overflow:hidden}

.header{position:absolute;left:0;top:0;width:1200px;height:133px;background:var(--white)}
.brand{position:absolute;left:0;width:1200px;top:34px;text-align:center;font-size:52px;font-weight:700;letter-spacing:6px;color:#5a5a5a;text-transform:uppercase}

.topbar{position:absolute;left:0;top:133px;width:1200px;height:52px;background:var(--bar)}
.search{position:absolute;left:30px;top:18px;width:133px;height:19px;background:var(--white);border:1px solid #111;font-size:11px;font-weight:700;line-height:17px;padding-left:5px;color:#111}
.search svg{position:absolute;right:0;top:0;width:22px;height:17px;border-left:1px solid #111}
.main-nav{position:absolute;left:253px;top:0;height:52px;display:flex;list-style:none}
.main-nav li{font-size:15px;font-weight:600;color:var(--white);line-height:52px;margin-right:27px;position:relative}
.main-nav li.is-active::after{content:"";position:absolute;left:-10px;right:-10px;bottom:0;height:4px;background:var(--accent-green)}
.social{position:absolute;left:1013px;top:14px;display:flex;gap:10px}
.social span{width:24px;height:24px;background:var(--social);border-radius:3px}

.sidebar{position:absolute;left:0;top:185px;width:210px;height:815px;background:var(--white)}
.side-nav{list-style:none;position:absolute;top:78px;left:0;width:208px}
.side-nav li{height:32px;line-height:30px;text-align:center;font-size:16px;font-weight:600;color:var(--ink-soft);text-transform:uppercase}
.side-nav li.is-current{background:var(--nav-active)}
.tweets-title{position:absolute;left:17px;top:292px;font-size:16px;font-weight:700;color:#333}
.tweet{position:absolute;left:12px;width:195px;display:flex;gap:12px}
.tweet-icon{flex:none;width:34px;height:34px;border-radius:50%;background:var(--tweet);display:flex;align-items:center;justify-content:center}
.tweet p{font-size:15px;line-height:24px;color:var(--ink)}
.copyright{position:absolute;left:0;width:210px;top:743px;text-align:center;font-size:11px;line-height:19px;color:var(--ink-soft);text-transform:uppercase}

.tile{position:absolute;color:var(--white)}
.photo{position:absolute}
.photo-deck{left:210px;top:185px;width:325px;height:200px;background:linear-gradient(160deg,#6b7a5a,#3a3226 55%,#a8845a)}
.photo-garden{left:862px;top:185px;width:338px;height:200px;background:linear-gradient(150deg,#1c2430,#4a3a22 55%,#8a6a3a)}
.photo-stone{left:210px;top:385px;width:257px;height:168px;background:linear-gradient(140deg,#2a2420,#6a4a2a 50%,#3a3a22)}
.photo-kitchen{left:210px;top:553px;width:257px;height:167px;background:linear-gradient(160deg,#4a3a30,#3a3634 50%,#8a6a4a)}
.photo-night{left:467px;top:385px;width:312px;height:335px;background:linear-gradient(170deg,#2c3038,#1a1a1a 60%,#242018)}
.photo-lights{left:779px;top:385px;width:249px;height:335px;background:linear-gradient(170deg,#2a4a7a,#1e2a30 50%,#4a4a22)}
.photo-kitchen-side{left:1028px;top:385px;width:172px;height:176px;background:linear-gradient(160deg,#4a3430,#5a4a40 50%,#7a5030)}
.photo-apartment{left:210px;top:720px;width:539px;height:280px;background:linear-gradient(180deg,#3a6ac8,#8a8a8a 45%,#6a625a)}
.dark-fill{left:749px;top:720px;width:451px;height:280px;background:var(--dark)}

.box-orange{left:535px;top:185px;width:327px;height:200px;background:var(--orange);padding:26px 12px 0 17px}
.box-orange h2{font-size:31px;line-height:40px;font-weight:700;text-align:center;text-transform:uppercase}
.box-orange p{font-size:15px;line-height:21px;margin-top:5px}
.box-variety{left:492px;top:528px;width:270px}
.box-variety h2{font-size:32px;font-weight:700;line-height:40px}
.box-variety p{font-size:15px;line-height:22px;margin-top:6px}
.box-purple{left:779px;top:385px;width:172px;height:160px;background:var(--purple);padding:27px 8px 0 20px}
.box-purple p{font-size:15px;line-height:24px}
.box-purple h3{font-size:21px;line-height:30px;font-weight:600;text-align:center;margin-left:-12px;text-transform:uppercase}
.box-lime{left:1028px;top:561px;width:172px;height:159px;background:var(--lime);padding:34px 10px 0 27px}
.box-lime h3{font-size:15px;font-weight:700;line-height:22px;text-align:center;margin-left:-17px;text-transform:uppercase}
.box-lime p{font-size:15px;line-height:24px}
.box-sky{left:749px;top:720px;width:384px;height:197px;background:var(--sky);padding:11px 12px 0 17px}
.box-sky h2{font-size:31px;line-height:33px;font-weight:700;text-transform:uppercase}
.box-sky p{font-size:15px;line-height:22px;margin-top:7px}
</style>
</head>
<body>
<div class="canvas">
  <header class="header">
    <div class="brand">Lumo Vant</div>
  </header>

  <nav class="topbar">
    <div class="search">SEARCH
      <svg viewBox="0 0 22 17"><circle cx="10" cy="7.5" r="4" fill="none" stroke="#111" stroke-width="2"/><line x1="13" y1="10.5" x2="16.5" y2="14" stroke="#111" stroke-width="2"/></svg>
    </div>
    <ul class="main-nav">
      <li>VIEW</li><li class="is-active">ALL</li><li>AUDIO</li><li>OTHER</li><li>PHOTO</li><li>WEB</li>
    </ul>
    <div class="social"><span></span><span></span><span></span><span></span><span></span></div>
  </nav>

  <aside class="sidebar">
    <ul class="side-nav">
      <li class="is-current">Home</li><li>Gallery</li><li>Portfolio</li><li>Blog</li><li>Contacts</li>
    </ul>
    <h4 class="tweets-title">RECENT TWEETS</h4>
    <div class="tweet" style="top:327px">
      <div class="tweet-icon"><svg width="16" height="16" viewBox="0 0 16 16"><circle cx="8" cy="8" r="5" fill="#fff"/></svg></div>
      <p>Lorem ipsum dolor adipiscing elit. Niih cursrtus a, elefend.</p>
    </div>
    <div class="tweet" style="top:407px">
      <div class="tweet-icon"><svg width="16" height="16" viewBox="0 0 16 16"><circle cx="8" cy="8" r="5" fill="#fff"/></svg></div>
      <p>Lorem ipsum dolor adipiscing elit. Niih cursrtus a, elefend.</p>
    </div>
    <div class="copyright">Copyright © Lumovant<br>All right reserved.</div>
  </aside>

  <main>
    <div class="photo photo-deck" role="img" aria-label="Timber deck with steps and garden lights at dusk"></div>
    <div class="photo photo-garden" role="img" aria-label="Lit house and garden at night"></div>
    <div class="photo photo-stone" role="img" aria-label="Stone wall house entry at night"></div>
    <div class="photo photo-kitchen" role="img" aria-label="Modern kitchen with downlights"></div>
    <div class="photo photo-night" role="img" aria-label="House exterior at night"></div>
    <div class="photo photo-lights" role="img" aria-label="Garden plants lit at dusk"></div>
    <div class="photo photo-kitchen-side" role="img" aria-label="Kitchen bench with timber floor"></div>
    <div class="photo photo-apartment" role="img" aria-label="Modern apartment building with balconies under blue sky"></div>
    <div class="photo dark-fill"></div>

    <section class="tile box-orange">
      <h2>Choose a best way of living</h2>
      <p>Lorem ipsum dolor sit amet, consectetur adipiscing elit. Niihunclorem est, eleifend cursrtus a, elefend in nunc. Nulla fagcigisi.</p>
    </section>
    <section class="tile box-variety">
      <h2>VARIETY</h2>
      <p>Lorem ipsum dolor sit amet, adipiscing elit. Niihunclorem est.</p>
    </section>
    <section class="tile box-purple">
      <p>Lorem ipsum sit adipiscing elit.</p>
      <h3>Innovative light houses</h3>
    </section>
    <section class="tile box-lime">
      <h3>Moderenize kichen</h3>
      <p>Lorem ipsum sit adipiscing elit.</p>
    </section>
    <section class="tile box-sky">
      <h2>Different color scheme apartment</h2>
      <p>Lorem ipsum dolor sit amet,<br>adipiscing elit. Niihunclorem est.</p>
    </section>
  </main>
</div>
</body>
</html>
```